Velora Aesthetica

Medical doctor providing aesthetic medicine

* Double sided card
* Logo to be on card
Other details:
* Dr. Mirela Kostvan, BSc, MBChB, CCFP
* #214-215, 27903 83 Ave, Surrey, BC, V2T 4K7
* 604-718-2943
* info@veloraclinic.ca
* www.veloraclinic.ca

Industry/Entity Type

Medical / Health & Beauty

Contact Information for Business Card

see 'Project Description'

Colors
0054AA
0677BA
7BADD7
CADEEF
E8F1F8
FFF300
FFF600
FEFA6F
FFFEC7
FFFEE8

Requirements
Must have
• Modern, high-end design

```html
<!DOCTYPE html>
<html lang="en">
<head>
<meta charset="utf-8">
<title>Velora Aesthetica – Business Card</title>
<link rel="stylesheet" href="https://fonts.googleapis.com/css2?family=Montserrat:wght@400;500;700&display=swap">
<style>
  :root {
    --stage: #222222;
    --card: #ffffff;
    --ink: #1a1a1a;
    --gold: #d1a92a;
    --gold-light: #e9c43c;
    --gold-deep: #b8901f;
    --muted: #2b2b2b;
  }
  * { box-sizing: border-box; margin: 0; padding: 0; }
  html, body {
    width: 1200px; height: 711px; overflow: hidden;
    background: var(--stage);
    font-family: "Montserrat", sans-serif;
  }
  .stage {
    position: relative; width: 1200px; height: 711px;
    display: flex; justify-content: center; align-items: center; gap: 90px;
  }
  .card {
    position: relative;
    width: 340px; height: 580px;
    background: var(--card);
    border-radius: 30px;
    box-shadow: 0 10px 24px rgba(0,0,0,.45);
    overflow: hidden;
  }

  /* Front: name runs along the long side */
  .card--front {
    display: flex; align-items: center; justify-content: center; gap: 34px;
    padding-right: 20px;
  }
  .card--front .brand-name {
    writing-mode: vertical-rl;
    font-size: 34px; letter-spacing: 9px;
    white-space: nowrap;
  }
  .brand-mark {
    width: 130px; height: 130px; border-radius: 50%;
    border: 3px solid var(--gold);
    flex: none;
  }
  .brand-name {
    font-weight: 500; color: var(--ink);
    text-transform: uppercase; text-align: center;
  }

  /* Back */
  .card--back {
    display: flex; flex-direction: column; align-items: center;
    padding-top: 56px; text-align: center;
  }
  .card--back .brand-mark { width: 82px; height: 82px; border-width: 2.5px; margin-bottom: 20px; }
  .card--back .brand-name { font-size: 21px; letter-spacing: 5px; }
  .doctor {
    margin-top: 50px;
    font-weight: 700; font-size: 22px; color: var(--gold);
  }
  .credentials { font-size: 12.5px; color: var(--muted); margin-top: 4px; }

  .divider {
    display: flex; align-items: center; gap: 6px;
    width: 310px; margin: 16px 0 10px;
  }
  .divider__band {
    flex: 1; height: 10px; border-radius: 5px;
  }
  .divider__band--left  { background: linear-gradient(90deg, rgba(209,169,42,0) 0%, var(--gold) 100%); }
  .divider__band--right { background: linear-gradient(90deg, var(--gold) 0%, rgba(209,169,42,0) 100%); }
  .icon {
    width: 26px; height: 26px; border-radius: 50%;
    background: linear-gradient(180deg, var(--gold-light), var(--gold-deep));
    display: flex; align-items: center; justify-content: center; flex: none;
  }
  .icon svg { width: 16px; height: 16px; display: block; }

  .contact-list { list-style: none; font-size: 13px; color: var(--muted); line-height: 1.5; }
  .address { font-style: normal; font-size: 13px; color: var(--muted); line-height: 1.5; }
</style>
</head>
<body>
<main class="stage">

  <section class="card card--front" aria-label="Card front">
    <p class="brand-name">Velora Aesthetica</p>
    <div class="brand-mark" aria-hidden="true"></div>
  </section>

  <section class="card card--back" aria-label="Card back">
    <div class="brand-mark" aria-hidden="true"></div>
    <p class="brand-name">Velora Aesthetica</p>

    <h1 class="doctor">Dr. Mirela Kostvan</h1>
    <p class="credentials">BSc, MBChB, CCFP</p>

    <div class="divider">
      <div class="divider__band divider__band--left" role="img" aria-label="Gold graduated dot divider"></div>
      <span class="icon" aria-hidden="true">
        <svg viewBox="0 0 16 16"><path d="M4 2.5 q-2 1 0 5 q3 6 8 7 q2 0 2.5-2 l-3-2 -1.5 1 q-3-1-4-4 l1-1.5z" fill="#fff"/></svg>
      </span>
      <span class="icon" aria-hidden="true">
        <svg viewBox="0 0 16 16" fill="none" stroke="#fff" stroke-width="1.4"><rect x="1.5" y="3.5" width="13" height="9" rx="1"/><polyline points="1.5,3.5 8,9 14.5,3.5"/></svg>
      </span>
      <span class="icon" aria-hidden="true">
        <svg viewBox="0 0 16 16" fill="none" stroke="#fff" stroke-width="1.2"><circle cx="8" cy="8" r="6.5"/><ellipse cx="8" cy="8" rx="2.8" ry="6.5"/><line x1="1.5" y1="8" x2="14.5" y2="8"/></svg>
      </span>
      <div class="divider__band divider__band--right" role="img" aria-label="Gold graduated dot divider"></div>
    </div>

    <ul class="contact-list">
      <li>604-718-2943</li>
      <li>info@veloraclinic.ca</li>
      <li>www.veloraclinic.ca</li>
    </ul>

    <div class="divider">
      <div class="divider__band divider__band--left" role="img" aria-label="Gold graduated dot divider"></div>
      <span class="icon" aria-hidden="true">
        <svg viewBox="0 0 16 16"><path d="M8 15 q-5.5-6-5.5-9.5 a5.5 5.5 0 0 1 11 0 q0 3.5-5.5 9.5z" fill="#fff"/><circle cx="8" cy="5.5" r="2" fill="#d1a92a"/></svg>
      </span>
      <div class="divider__band divider__band--right" role="img" aria-label="Gold graduated dot divider"></div>
    </div>

    <address class="address">#214-215, 27903 83 Ave,<br>Surrey, BC, V2T 4K7</address>
  </section>

</main>
</body>
</html>
```